Build our new website pages and templates

BACKGROUND
• We are migrating over from an old website and URL ( www.plotwharf.co.nz ) to a brand new website with a new URL – www.galbrook.co.nz
• We have already selected a logo for the new website – see attached.
• We manage all our websites in house using Dreamweaver and want to retain the capability of doing this for the new site.

-------------------------------------------------------------------------------------

BRIEF
• Design the new look galbrook website for our company including color palette, fonts, icons, graphics and layout.

• The design should reflect our high quality venue hire services to corporate buyers, picking up inspiration from our beautiful new logo

• The index page should also incorporate our:

o What We Do page
o How To Use Our Site page
o Are you a venue? content (with link to the 'List A Venue' page)
o Our key contact links
o Our navigation menu

Here are some examples of the types of Index pages that appeal to us:

http://wheretilesdrop.com/
What we like about it: Like the simplicity of the page and the scroll function to show different page elements.

http://www.qarvo.com/
What we like about it: Strong blocks of hero images and fonts. Easy scroll from one section to the next.

https://www.lumt.com/
What we like about it: Like the scroll feature to different sections.

https://www.pondtable.net/
What we like about it: Simple stylish Index page that scrolls easily

Our version would be:
1. Our logo centre page with hero image background
2. Scroll down to 'what we do' section with 3 bullet points and icons
3. Scroll down to 'how to use this site' section with 3 bullet points (1,2,3) and instructions
4. Are you a venue? instructions about how to talk to us about listing. And link to the 'how to list' page.

To the left we would want a burger menu with dropdown nav and links

• Design the template for the 'venue listings' pages
o We want to list venues by towns or cities and have one page dedicated for each. We would create each page from the template you provide.
o When the user clicks on any particular venue it clicks through to the individual venue page
o This page should have a map with pins for each listed venue

Here are some examples of the listings pages that we like and why:

http://www.qarvo.com/
What we like about it: Strong blocks and font. Nice hover feature changing the colour and introducing the click through arrow on the right bottom corner

http://www.gatherloft.co.nz/
What we like about it: Don’t like the colours or design but like the practicality of the search box and the 3 column listings when you select a search criteria. This is a familiar format and maybe easier for the user to understand and navigate around.

http://www.tidemarkhalls.co.nz/venues
What we like about it: Like the simplicity of this page but our listings would need a little more info beneath each one. The hover function is annoying!

• Design the template for the individual venue pages.
• Include a search function across the full site so that users can choose to search for venues in different towns or cities.
• Design the booking form pages for the individual venues (we have working examples of our existing ones)

• Design the payment page and thank you page for those who complete the booking form online. (We will be offering the option on our site to pay by credit card into our coinwell account) We have working examples of our current thank you and payment page although the payment page is not live on our current site.

------------------------------------------------------------------------------------

TECHNICAL
• Pages need to be created in html and css. Some php pages, as required for payment pages. And some javascript for all pages.

• Templates will need to be in dwt format, as we need to be able to upload to Dreamweaver CC and create new pages from the templates for new venues as and when necessary.

• Pages should be responsive for browsing across PC’s Laptops, ipads, phones and other devices.

• Website will be hosted on a Linux server when ready to go live.

A) We can provide existing website files if these help with the design and build process of the new site.
B) We plan to build additional features for the site, as a second phase project. This would include client login areas and electronic confirmations of bookings and online updating of booking forms.

Requirements
Must have
• See the brief provided. Successful designer/developer must be able to supply files in html, css, php (if required) and include javascript coding where necessary. We will be hosting these files and managing the site using Dreamweaver CC so full accessibility to the files is important.
Nice to have
• Notes have been added to the brief. Please read and ask questions if not clear.
Should not have
• We are not looking for a site to be built using an open source platform. The files provided must be able to be uploaded to our own server for our own management after the end of the project.

```html
<!DOCTYPE html>
<html lang="en">
<head>
<meta charset="utf-8">
<title>Galbrook – Finding Venues For You</title>
<link href="https://fonts.googleapis.com/css2?family=Raleway:wght@500;600;700;800&family=Open+Sans:wght@400;600;700&display=swap" rel="stylesheet">
<style>
:root{
  --ink:#231f20;
  --ink-deep:#1a1718;
  --white:#ffffff;
  --green:#a0b62c;
  --green-icon:#8fb03a;
  --text:#444044;
  --muted:#7a7679;
  --step:#8c8a8b;
}
*{box-sizing:border-box;margin:0;padding:0}
html,body{width:697px;height:1200px;overflow:hidden}
body{position:relative;font-family:"Open Sans",sans-serif;background:var(--white);color:var(--text)}
.abs{position:absolute}
.head-font{font-family:"Raleway",sans-serif}

/* header */
.topbar{left:0;top:0;width:697px;height:50px;background:var(--ink)}
.menu-btn{left:57px;top:12px;width:26px;height:26px;border:1.5px solid var(--white);border-radius:50%}
.search-btn{left:629px;top:18px}
.brand-bowl{left:288px;top:-29px;width:122px;height:122px;border-radius:50%;background:var(--ink);z-index:3}
.brand-name{left:0;top:45px;width:122px;text-align:center;color:var(--white);font-family:"Raleway",sans-serif;font-weight:500;font-size:15px;letter-spacing:1px}
.brand-tag{left:0;top:70px;width:122px;text-align:center;color:#c9c6c7;font-size:4.5px;letter-spacing:.6px}

/* hero */
.hero{left:0;top:50px;width:697px;height:294px;background:linear-gradient(160deg,#5c3b22 0%,#8a5a32 35%,#4a2c18 70%,#2e1b10 100%)}
.hero-title{left:0;top:148px;width:697px;text-align:center;color:var(--white);font-family:"Raleway",sans-serif;font-weight:800;font-size:33px;letter-spacing:.5px;text-shadow:0 1px 4px rgba(0,0,0,.5)}
.hero-btn{top:198px;width:116px;height:26px;background:rgba(20,16,14,.85);border:1.5px solid var(--white);color:var(--white);font-family:"Raleway",sans-serif;font-weight:700;font-size:10px;display:flex;align-items:center;justify-content:center}
.hero-arrow{top:186px}

/* what we do */
.section-title{width:697px;left:0;text-align:center;font-family:"Raleway",sans-serif;font-weight:700;font-size:22px;color:var(--ink);letter-spacing:.5px}
.service{width:170px;text-align:center}
.service-icon{display:block;margin:0 auto}
.service-name{font-family:"Raleway",sans-serif;font-weight:600;font-size:11.5px;color:var(--ink);line-height:14.5px;margin-top:10px}
.service-text{font-size:7.3px;color:var(--muted);line-height:12.8px;margin-top:3px}
.read-more{font-size:7.3px;font-weight:700;color:var(--green);letter-spacing:.4px;margin-top:7px}

/* how to */
.howto{left:0;top:585px;width:697px;height:271px;background:#141213}
.howto-photo{left:348px;top:585px;width:349px;height:271px;background:linear-gradient(180deg,#1d2038 0%,#3b3450 30%,#6a5540 60%,#2a2226 100%)}
.howto-title{left:57px;top:609px;color:var(--white);font-family:"Raleway",sans-serif;font-weight:700;font-size:22px}
.step{left:57px;width:240px}
.step-num{position:absolute;left:0;top:0;width:28px;height:28px;border-radius:50%;background:var(--step);color:var(--white);font-weight:700;font-size:13px;display:flex;align-items:center;justify-content:center}
.step-name{position:absolute;left:40px;top:-4px;color:var(--white);font-family:"Raleway",sans-serif;font-weight:600;font-size:11px;white-space:nowrap}
.step-text{position:absolute;left:40px;top:13px;width:205px;color:#e4e2e3;font-size:7px;line-height:12.5px}
.howto-more{left:57px;top:823px;color:var(--white);font-size:7.5px;font-weight:700}

/* venue band */
.venue-band{left:0;top:856px;width:697px;height:150px;background:var(--green)}
.band-dot{left:324px;top:831px;width:50px;height:50px;border-radius:50%;background:var(--green)}
.band-title{top:886px;color:var(--white)}
.band-text{left:0;top:923px;width:697px;text-align:center;color:var(--white);font-size:8.6px;font-weight:600}
.band-btn{left:288px;top:952px;width:121px;height:24px;border:1.5px solid var(--white);color:var(--white);font-family:"Raleway",sans-serif;font-weight:700;font-size:9px;display:flex;align-items:center;justify-content:center}

/* footer */
.footer{left:0;top:1006px;width:697px;height:164px;background:var(--ink)}
.foot-brand{left:50px;top:1110px;width:120px;text-align:center;color:var(--white);font-family:"Raleway",sans-serif;font-weight:500;font-size:20px;letter-spacing:1px}
.foot-tag{left:50px;top:1135px;width:120px;text-align:center;color:#bdb9ba;font-size:5.5px;letter-spacing:.8px}
.foot-head{top:1027px;color:var(--white);font-family:"Raleway",sans-serif;font-weight:600;font-size:10.5px}
.quick-links{left:207px;top:1049px;list-style:none}
.quick-links li{color:var(--white);font-size:7px;height:17.6px;padding-left:13px;position:relative}
.quick-links li::before{content:"›";position:absolute;left:0;top:-2px;font-size:9px}
.foot-text{color:var(--white);font-size:7px;line-height:12.8px}
.field{left:329px;width:152px;height:20px;background:var(--white);color:#9a9697;font-size:6.5px;padding:6px 0 0 10px}
.subscribe{left:329px;top:1127px;width:73px;height:20px;border:1.5px solid var(--white);color:var(--white);font-size:6.5px;font-weight:700;display:flex;align-items:center;justify-content:center}
.copy-bar{left:0;top:1170px;width:697px;height:30px;background:var(--ink-deep)}
.copy{left:0;top:1180px;width:697px;text-align:center;color:var(--white);font-size:6.8px}
</style>
</head>
<body>

<header>
  <div class="abs topbar"></div>
  <div class="abs menu-btn">
    <svg width="23" height="23" viewBox="0 0 23 23"><g fill="#fff"><rect x="7.5" y="7.5" width="8" height="1.6"/><rect x="7.5" y="10.7" width="8" height="1.6"/><rect x="7.5" y="13.9" width="8" height="1.6"/></g></svg>
  </div>
  <svg class="abs search-btn" width="14" height="14" viewBox="0 0 14 14"><circle cx="5.8" cy="5.8" r="3.8" fill="none" stroke="#fff" stroke-width="1.8"/><line x1="8.6" y1="8.6" x2="11.5" y2="11.5" stroke="#fff" stroke-width="2" stroke-linecap="round"/></svg>
  <div class="abs brand-bowl">
    <div class="abs brand-name">GALBROOK</div>
    <div class="abs brand-tag">FINDING VENUES FOR YOU</div>
  </div>
</header>

<section>
  <div class="abs hero" role="img" aria-label="Photo of a boardroom with a long wooden table, leather chairs and a projection screen"></div>
  <h1 class="abs hero-title">FINDING VENUES FOR YOU</h1>
  <a class="abs hero-btn" style="left:155px">SEARCH VENUES</a>
  <a class="abs hero-btn" style="left:290px">WHAT WE DO</a>
  <a class="abs hero-btn" style="left:426px">LIST A VENUE</a>
  <svg class="abs hero-arrow" style="left:29px" width="14" height="22" viewBox="0 0 14 22"><polyline points="11,2 3,11 11,20" fill="none" stroke="#bbb" stroke-width="2"/></svg>
  <svg class="abs hero-arrow" style="left:654px" width="14" height="22" viewBox="0 0 14 22"><polyline points="3,2 11,11 3,20" fill="none" stroke="#bbb" stroke-width="2"/></svg>
  <svg class="abs" style="left:338px;top:290px" width="22" height="12" viewBox="0 0 22 12"><polyline points="2,2 11,10 20,2" fill="none" stroke="#ddd" stroke-width="2"/></svg>
</section>

<section>
  <h2 class="abs section-title" style="top:377px">WHAT WE DO</h2>

  <div class="abs service" style="left:50px;top:426px">
    <svg class="service-icon" width="32" height="36" viewBox="0 0 32 36" fill="#8fb03a"><rect x="1" y="5" width="30" height="30" rx="2"/><rect x="7" y="1" width="3" height="8" rx="1"/><rect x="22" y="1" width="3" height="8" rx="1"/><g fill="#fff"><rect x="4" y="13" width="5" height="4"/><rect x="10.5" y="13" width="5" height="4"/><rect x="17" y="13" width="5" height="4"/><rect x="23.5" y="13" width="5" height="4"/><rect x="4" y="19.5" width="5" height="4"/><rect x="10.5" y="19.5" width="5" height="4"/><rect x="17" y="19.5" width="5" height="4"/><rect x="23.5" y="19.5" width="5" height="4"/><rect x="4" y="26" width="5" height="4"/><rect x="10.5" y="26" width="5" height="4"/><rect x="17" y="26" width="5" height="4"/><rect x="23.5" y="26" width="5" height="4"/></g></svg>
    <div class="service-name">CONFERENCE &amp;<br>EVENT ORGANISERS</div>
    <div class="service-text">We provide venue options for your meetings,<br>conferences and events based</div>
    <div class="read-more">READ MORE &gt;&gt;</div>
  </div>

  <div class="abs service" style="left:264px;top:426px">
    <svg class="service-icon" width="42" height="36" viewBox="0 0 42 36" fill="#8fb03a" stroke="#fff" stroke-width="1.2"><polygon points="21,2 30,6 30,15 21,19 12,15 12,6"/><polygon points="12,16 21,20 21,29 12,33 3,29 3,20"/><polygon points="30,16 39,20 39,29 30,33 21,29 21,20"/></svg>
    <div class="service-name" style="margin-top:14px">ONE STOP SHOP</div>
    <div class="service-text">We take care of all the venue, catering, AV,<br>theming, travel, transport and accommodation<br>bookings on your behalf.</div>
    <div class="read-more">READ MORE &gt;&gt;</div>
  </div>

  <div class="abs service" style="left:476px;top:426px">
    <svg class="service-icon" width="38" height="36" viewBox="0 0 38 36" fill="#8fb03a"><circle cx="8" cy="8" r="5"/><circle cx="30" cy="8" r="5"/><circle cx="19" cy="11" r="6.5"/><path d="M1 24c0-6 3-9 7-9s6 2 6 4v5z"/><path d="M37 24c0-6-3-9-7-9s-6 2-6 4v5z"/><path d="M8 34c0-10 4-15 11-15s11 5 11 15z"/></svg>
    <div class="service-name" style="margin-top:14px">TRUSTED ADVISORS</div>
    <div class="service-text">We only list and recommend venues that are<br>personally checked by us to ensure the highest<br>quality for you.</div>
    <div class="read-more">READ MORE &gt;&gt;</div>
  </div>
</section>

<section>
  <div class="abs howto"></div>
  <div class="abs howto-photo" role="img" aria-label="Photo of a long candlelit dining table set with glasses beside waterfront windows at night"></div>
  <h2 class="abs howto-title">HOW TO USE THIS SITE</h2>

  <div class="abs step" style="top:652px">
    <div class="step-num">1</div>
    <div class="step-name">SEARCH FOR VENUES</div>
    <div class="step-text">Search our venue listings for spaces that will work for your event.</div>
  </div>
  <div class="abs step" style="top:707px">
    <div class="step-num">2</div>
    <div class="step-name">AVAILABILITY CHECKS</div>
    <div class="step-text">Contact us for a list of suitable and available spaces for your meetings, conferences and events.</div>
  </div>
  <div class="abs step" style="top:762px">
    <div class="step-num">3</div>
    <div class="step-name">BOOK ONLINE</div>
    <div class="step-text">Use our online booking system to confirm the details of your event and to make payment.</div>
  </div>
  <div class="abs howto-more">READ MORE &gt;&gt;</div>
</section>

<section>
  <div class="abs venue-band"></div>
  <div class="abs band-dot"></div>
  <h2 class="abs section-title band-title">ARE YOU A VENUE?</h2>
  <p class="abs band-text">If you would like to list your spaces on GALBROOK click here for listing options and packages.</p>
  <a class="abs band-btn">LIST A VENUE</a>
</section>

<footer>
  <div class="abs footer"></div>
  <div class="abs foot-brand">GALBROOK</div>
  <div class="abs foot-tag">FINDING VENUES FOR YOU</div>

  <h3 class="abs foot-head" style="left:207px">Quick links</h3>
  <ul class="abs quick-links">
    <li>Home</li>
    <li>Auckland Venues</li>
    <li>Waiheke Venues</li>
    <li>Rakino Island</li>
    <li>Wellington Venues</li>
    <li>Sydney Venues</li>
  </ul>

  <h3 class="abs foot-head" style="left:329px">Contact us</h3>
  <svg class="abs" style="left:330px;top:1048px" width="12" height="11" viewBox="0 0 12 11"><polygon points="0,5 12,0 9,11 6,8 4,10 4,7" fill="#fff"/></svg>
  <p class="abs foot-text" style="left:348px;top:1046px;width:140px">Sign up with your name and email to get updates fresh updates.</p>
  <div class="abs field" style="top:1077px">Name</div>
  <div class="abs field" style="top:1102px">Email id</div>
  <a class="abs subscribe">SUBSCRIBE NOW</a>

  <h3 class="abs foot-head" style="left:526px">Get In Touch</h3>
  <svg class="abs" style="left:527px;top:1050px" width="10" height="9" viewBox="0 0 10 9"><polygon points="5,0 10,4.5 8.5,4.5 8.5,9 1.5,9 1.5,4.5 0,4.5" fill="#fff"/></svg>
  <p class="abs foot-text" style="left:545px;top:1048px;width:100px">45 BC. This book is a treatise on the theory of ethics</p>
  <svg class="abs" style="left:527px;top:1091px" width="9" height="9" viewBox="0 0 9 9"><path d="M1 0h2l1 2.2-1.2 1a5 5 0 0 0 3 3l1-1.2L9 6v2a1 1 0 0 1-1 1A8 8 0 0 1 0 1a1 1 0 0 1 1-1z" fill="#fff"/></svg>
  <p class="abs foot-text" style="left:545px;top:1089px">+152 207 300 5716</p>
  <svg class="abs" style="left:527px;top:1123px" width="10" height="7" viewBox="0 0 10 7"><rect width="10" height="7" rx="1" fill="#fff"/><polyline points="0.5,0.5 5,4 9.5,0.5" fill="none" stroke="#231f20" stroke-width="0.9"/></svg>
  <p class="abs foot-text" style="left:545px;top:1120px">info@galbrook.in</p>

  <div class="abs copy-bar"></div>
  <p class="abs copy">Copyright © 2016, Galbrook. All Rights Reserved</p>
</footer>

</body>
</html>
```